Mental health agency needs an ad for brochure

Please provide us with a half page (W 8.5 inches x H 5.5 inches) advertising our company. We are a mental health agency that provides training, education, and consultation for companies that serve children, adolescents, or adults. We can offer training and education to help companies better serve their clientele and consultation about how companies are currently working with their staff or clientele. Our website is www.quellbrook.com and they can contact us at info@haverstoneinstitute.com or 503-847-2163.

```html
<!DOCTYPE html>
<html lang="en">
<head>
<meta charset="UTF-8">
<title>Haverstone Institute – Brochure Ad</title>
<link href="https://fonts.googleapis.com/css2?family=Lexend:wght@500;600;700&family=Raleway:wght@400;500;700&display=swap" rel="stylesheet">
<style>
  :root {
    --navy: #0c2d6b;
    --teal: #07a0c8;
    --card-top: #0a5a92;
    --card-bottom: #1596c4;
    --ink: #1b1b1b;
    --white: #ffffff;
    --photo-light: #f1ece4;
    --photo-mid: #d9cbb7;
  }
  * { margin: 0; padding: 0; box-sizing: border-box; }
  html, body { width: 885px; height: 1200px; overflow: hidden; background: var(--white); }
  .ad {
    position: relative;
    width: 885px;
    height: 1200px;
    overflow: hidden;
    background: var(--white);
    font-family: "Raleway", sans-serif;
  }
  .hero { position: absolute; left: 0; top: 0; width: 885px; height: 500px; }
  .brand-box {
    position: absolute;
    left: 110px; top: 78px;
    width: 278px; height: 207px;
    background: var(--white);
    border: 2px solid var(--teal);
    border-radius: 22px;
    display: flex; flex-direction: column;
    align-items: center; justify-content: center;
    gap: 16px;
  }
  .brand-dot { width: 64px; height: 64px; border-radius: 50%; background: var(--navy); }
  .brand-name {
    font-family: "Raleway", sans-serif;
    font-weight: 700;
    font-size: 23px;
    color: var(--navy);
    letter-spacing: 0.5px;
  }
  .headline {
    position: absolute;
    left: 74px; top: 346px;
    font-family: "Lexend", sans-serif;
    font-weight: 600;
    font-size: 35px;
    line-height: 44px;
    color: var(--navy);
  }
  .divider {
    position: absolute;
    left: 74px; top: 508px;
    width: 756px;
    border-top: 1px dotted var(--teal);
  }
  .divider-accent {
    position: absolute;
    left: 50px; top: -4px;
    width: 62px; height: 7px;
    background: var(--teal);
  }
  .intro {
    position: absolute;
    left: 74px; top: 528px;
    width: 756px;
    font-size: 18.5px;
    line-height: 25px;
    color: var(--ink);
    text-align: justify;
    font-weight: 500;
  }
  .section-tag {
    position: absolute;
    left: 69px; top: 648px;
    width: 263px; height: 29px;
    background: var(--navy);
    color: var(--white);
    border-radius: 7px;
    font-family: "Lexend", sans-serif;
    font-weight: 600;
    font-size: 18px;
    line-height: 29px;
    text-align: center;
  }
  .service {
    position: absolute;
    top: 730px;
    width: 241px; height: 307px;
    border-radius: 24px;
    background: linear-gradient(180deg, var(--card-top), var(--card-bottom));
  }
  .service-notch {
    position: absolute;
    left: 50%; top: -36px;
    width: 94px; height: 76px;
    transform: translateX(-50%);
    background: var(--white);
    border-radius: 0 0 47px 47px;
  }
  .service-icon {
    position: absolute;
    left: 50%; top: -40px;
    width: 70px; height: 66px;
    transform: translateX(-50%);
  }
  .service-text {
    position: absolute;
    left: 8px; right: 8px; top: 48px;
    color: var(--white);
    font-size: 16.5px;
    line-height: 22px;
    text-align: center;
    font-weight: 400;
  }
  .service--training { left: 74px; }
  .service--therapy { left: 330px; }
  .service--staff { left: 588px; }
  .contact-label {
    position: absolute;
    left: 123px; top: 1072px;
    width: 203px;
    text-align: center;
    font-family: "Lexend", sans-serif;
    font-weight: 600;
    font-size: 26px;
    color: var(--teal);
  }
  .contact-frame { position: absolute; left: 118px; top: 1078px; width: 213px; height: 36px; }
  .contact-line {
    position: absolute;
    left: 364px;
    display: flex; align-items: center; gap: 12px;
    color: var(--navy);
  }
  .contact-line--phone { top: 1058px; font-family: "Lexend", sans-serif; font-weight: 700; font-size: 27px; }
  .contact-line--email { top: 1094px; font-size: 22px; font-weight: 500; }
  .contact-icon { width: 22px; height: 22px; flex: none; }
  .website {
    position: absolute;
    left: 0; width: 885px; top: 1150px;
    text-align: center;
    font-size: 22px;
    font-weight: 500;
    letter-spacing: 23px;
    padding-left: 23px;
    color: var(--navy);
  }
</style>
</head>
<body>
<div class="ad">
  <svg class="hero" viewBox="0 0 885 500" xmlns="http://www.w3.org/2000/svg">
    <defs>
      <linearGradient id="photoTone" x1="0" y1="0" x2="1" y2="1">
        <stop offset="0" stop-color="#e9ddcc"/>
        <stop offset="0.5" stop-color="#f4efe8"/>
        <stop offset="1" stop-color="#dfe3e6"/>
      </linearGradient>
    </defs>
    <rect class="hero-photo" x="0" y="0" width="885" height="360" fill="url(#photoTone)" role="img" aria-label="Photo of a smiling family of four embracing beside a bright window"/>
    <path class="wave-navy" fill="#0c2d6b" d="M391 245 L630 320 C700 342 760 318 800 270 C840 225 868 175 885 124 L885 320 L391 320 Z"/>
    <path class="wave-teal" fill="#07a0c8" d="M391 272 L620 345 C690 366 752 342 792 300 C832 258 860 215 885 172 L885 486 Z"/>
    <path class="wave-navy-left" fill="#0c2d6b" d="M0 85 L115 118 L115 150 C60 160 20 190 0 232 Z"/>
    <path class="wave-teal-left" fill="#07a0c8" d="M0 232 C20 190 60 160 115 150 L115 215 C60 218 22 268 0 350 Z"/>
    <path class="wave-white" fill="#ffffff" d="M0 350 C22 268 60 218 115 215 L391 284 L885 486 L885 500 L0 500 Z"/>
  </svg>

  <div class="brand-box">
    <div class="brand-dot"></div>
    <div class="brand-name">Haverstone Institute</div>
  </div>

  <h1 class="headline">Nurture Authentic<br>and Safe Relationships<br>Around You</h1>

  <div class="divider"><span class="divider-accent"></span></div>

  <p class="intro">We help trauma survivors overcome the experience of rejection, abandonment, and distrust by developing resources to become emotionally regulated in order to enjoy time with family and friends more confidently.</p>

  <div class="section-tag">WHAT WE PROVIDE</div>

  <div class="service service--training">
    <div class="service-notch"></div>
    <svg class="service-icon" viewBox="0 0 70 66" fill="none" stroke="#07a0c8" stroke-width="2.2" stroke-linecap="round" stroke-linejoin="round">
      <circle cx="35" cy="24" r="12"/>
      <path d="M14 62 C14 48 22 40 35 40 C48 40 56 48 56 62 Z"/>
      <path d="M22 42 L16 26 L24 16"/>
      <path d="M48 42 L54 26 L46 16"/>
      <path d="M22 6 l4 4 M35 3 v5 M48 6 l-4 4"/>
    </svg>
    <p class="service-text">Reduce stress and develop poise in managing behaviors in your school and non-profit child-serving organizations with training in the area of trauma and its effect on the brain and body.</p>
  </div>

  <div class="service service--therapy">
    <div class="service-notch"></div>
    <svg class="service-icon" viewBox="0 0 70 66" fill="none" stroke="#07a0c8" stroke-width="2.2" stroke-linecap="round" stroke-linejoin="round">
      <circle cx="35" cy="34" r="10"/>
      <path d="M18 64 C18 52 25 46 35 46 C45 46 52 52 52 64"/>
      <path d="M10 40 L14 52 L24 54 M60 40 L56 52 L46 54"/>
      <path d="M35 4 l2.5 5 5.5 .8 -4 3.9 1 5.5 -5-2.6 -5 2.6 1-5.5 -4-3.9 5.5-.8 z"/>
      <path d="M16 12 l1.6 3.3 3.6 .5 -2.6 2.5 .6 3.6 -3.2-1.7 -3.2 1.7 .6-3.6 -2.6-2.5 3.6-.5 z"/>
      <path d="M54 12 l1.6 3.3 3.6 .5 -2.6 2.5 .6 3.6 -3.2-1.7 -3.2 1.7 .6-3.6 -2.6-2.5 3.6-.5 z"/>
    </svg>
    <p class="service-text">Develop confidence and become self-assured to build strong and reliable boundaries in relationship with others using body-oriented therapy, offered for individuals, couples, and families.</p>
  </div>

  <div class="service service--staff">
    <div class="service-notch"></div>
    <svg class="service-icon" viewBox="0 0 70 66" fill="none" stroke="#07a0c8" stroke-width="2.2" stroke-linecap="round" stroke-linejoin="round">
      <circle cx="18" cy="16" r="13"/><circle cx="18" cy="13" r="4"/><path d="M10 25 C12 19 24 19 26 25"/>
      <circle cx="52" cy="16" r="13"/><circle cx="52" cy="13" r="4"/><path d="M44 25 C46 19 58 19 60 25"/>
      <circle cx="18" cy="50" r="13"/><path d="M12 50 l4 4 8-8"/>
      <circle cx="52" cy="50" r="13"/><circle cx="52" cy="47" r="4"/><path d="M44 59 C46 53 58 53 60 59"/>
      <path d="M28 40 L42 26"/>
    </svg>
    <p class="service-text">Decrease staff stress, burnout, and absenteeism while increasing staff authenticity and openness using feedback and heatmapping tools across teams and departments in your organization.</p>
  </div>

  <svg class="contact-frame" viewBox="0 0 213 36" fill="none" stroke="#0c2d6b" stroke-width="1.8" stroke-linecap="round">
    <path d="M2 2 L14 34 L199 34 L211 2"/>
  </svg>
  <div class="contact-label">Contact Us</div>

  <div class="contact-line contact-line--phone">
    <svg class="contact-icon" viewBox="0 0 24 24"><path fill="#07a0c8" d="M6.6 10.8a15.1 15.1 0 0 0 6.6 6.6l2.2-2.2a1 1 0 0 1 1-.25 11.4 11.4 0 0 0 3.6.57 1 1 0 0 1 1 1V20a1 1 0 0 1-1 1A17 17 0 0 1 3 4a1 1 0 0 1 1-1h3.5a1 1 0 0 1 1 1c0 1.25.2 2.45.57 3.57a1 1 0 0 1-.25 1z"/></svg>
    <span>503-847-2163</span>
  </div>
  <div class="contact-line contact-line--email">
    <svg class="contact-icon" viewBox="0 0 24 24" fill="none" stroke="#07a0c8" stroke-width="2"><rect x="2" y="5" width="20" height="14"/><path d="M2 5 L12 13 L22 5 M2 19 L9 11 M22 19 L15 11"/></svg>
    <span>info@haverstoneinstitute.com</span>
  </div>

  <div class="website">www.quellbrook.com</div>
</div>
</body>
</html>
```